Drone company needs a brochure design

We would like a brochure design which compliments our existing logo, website and business card designs.

www.tallowmerrin.com.au

Business

```html
<!DOCTYPE html>
<html lang="en">
<head>
<meta charset="utf-8">
<title>Tallow Merrin — Brochure Cover</title>
<link rel="stylesheet" href="https://fonts.googleapis.com/css2?family=Figtree:wght@500;700&display=swap">
<style>
  :root {
    --paper: #ffffff;
    --charcoal: #352f30;
    --sky: #3aa9df;
    --ink: #2f2a2b;
  }
  * { margin: 0; padding: 0; box-sizing: border-box; }
  html, body {
    width: 938px;
    height: 1200px;
    overflow: hidden;
    background: var(--paper);
  }
  .cover {
    position: relative;
    width: 938px;
    height: 1200px;
    font-family: "Figtree", Arial, sans-serif;
  }
  .cover-art {
    position: absolute;
    inset: 0;
    width: 938px;
    height: 1200px;
    display: block;
  }
  .brand {
    position: absolute;
    top: 400px;
    left: 0;
    width: 938px;
    display: flex;
    justify-content: center;
    align-items: center;
    gap: 18px;
  }
  .brand-mark {
    width: 30px;
    height: 30px;
    background: var(--sky);
  }
  .brand-name {
    font-weight: 500;
    font-size: 60px;
    line-height: 1;
    letter-spacing: 0.5px;
    color: var(--sky);
  }
  .tagline {
    position: absolute;
    top: 908px;
    left: 0;
    width: 938px;
    text-align: center;
    font-weight: 700;
    font-size: 24.5px;
    line-height: 39px;
    text-transform: uppercase;
    color: var(--ink);
    letter-spacing: 0.2px;
  }
</style>
</head>
<body>
  <main class="cover">
    <svg class="cover-art" viewBox="0 0 938 1200" aria-hidden="true">
      <rect class="cover-panel" x="15" y="15" width="907" height="1170" fill="var(--charcoal)"/>
      <polygon class="cover-peak" points="468,556 922,1006 922,1185 15,1185 15,1006" fill="var(--sky)"/>
    </svg>

    <header class="brand">
      <span class="brand-mark"></span>
      <span class="brand-name">Tallow Merrin</span>
    </header>

    <p class="tagline">
      We provide premium aerial media<br>
      solutions using the latest unmanned<br>
      aerial vehicles (UAV)&nbsp; technology.
    </p>
  </main>
</body>
</html>
```